Stylish Business Card for Modern hair salon

I need a simple business card design using our salon logo and colours that are in the logo. We service clients of all ages but predominantly those in the 18 to 55 age range. We have a young staff and are looking to have a card that will present a modern and clean image that represents who we are. The card should be in black and white same as our logo. Minimal use of other colours is allowed.

Industry/Entity Type

Hair And Beauty

Contact Information for Business Card

The design should have the following information
salon name - TR Hair Studio
address - 2751 Birchfield Rd.E. Cedarvale, QC H4R2M8
phone - 555 614-2870
website - trhairexample.ca
instagram - trhair.salon
twitter - @TRsalonCuts

Colors
000000
ffffff
474747

Requirements
Must have
• simple design, salon name, address, phone, website, instagram, twitter info
• Back of card should have the following:
• YOUR NEXT APPOINTMENT
• DATE
• TIME
Nice to have
• simple design, clear to see and read,
• predominantly black and white colour, minimal use of other colours is ok
Should not have
• many colours, various fonts

```html
<!DOCTYPE html>
<html lang="en">
<head>
<meta charset="utf-8">
<title>TR Hair Studio – Business Card</title>
<link href="https://fonts.googleapis.com/css2?family=Cormorant+Garamond:wght@500&display=swap" rel="stylesheet">
<style>
  :root {
    --ink: #000000;
    --paper: #ffffff;
    --grey: #474747;
    --backdrop: #e6e6e6;
  }
  * { box-sizing: border-box; margin: 0; padding: 0; }
  html, body {
    width: 1200px; height: 900px; overflow: hidden;
    background: var(--backdrop);
    font-family: "Cormorant Garamond", "Times New Roman", serif;
    font-weight: 500;
  }
  .canvas {
    width: 1200px; height: 900px;
    display: flex; flex-direction: column; align-items: center; justify-content: center;
    gap: 40px;
  }
  .card {
    width: 600px; height: 343px;
    position: relative;
    box-shadow: 0 6px 18px rgba(0,0,0,0.18);
  }
  /* Front */
  .card--front {
    background: var(--ink); color: var(--paper);
    display: flex; flex-direction: column; align-items: center;
    padding-top: 78px; text-align: center;
  }
  .brand-name {
    font-size: 52px; font-weight: 500; letter-spacing: 2px; line-height: 1;
  }
  .contact {
    margin-top: 62px;
    font-size: 16px; line-height: 1.35; letter-spacing: 0.3px;
  }
  .contact .sep { margin: 0 6px; }
  .social {
    margin-top: 8px;
    display: flex; gap: 34px; justify-content: center;
    font-size: 14px;
  }
  .social-item { display: flex; align-items: center; gap: 8px; }
  .social-dot {
    width: 9px; height: 9px; border: 1px solid var(--paper); border-radius: 50%;
  }
  /* Back */
  .card--back {
    background: var(--paper); color: var(--ink);
  }
  .appointment-title {
    position: absolute; top: 104px; left: 0; right: 0;
    text-align: center; font-size: 24px; font-weight: 500; letter-spacing: 0.5px;
  }
  .appointment-fields {
    position: absolute; top: 172px; left: 40px; right: 40px;
    display: flex; align-items: flex-end; gap: 10px;
    font-size: 24px;
  }
  .field-line { border-bottom: 1px solid var(--ink); height: 1px; margin-bottom: 7px; }
  .field-line--date { flex: 1.9; }
  .field-line--time { flex: 1; }
  .back-band {
    position: absolute; left: 0; right: 0; bottom: 0; height: 36px;
    background: var(--ink);
  }
</style>
</head>
<body>
<main class="canvas">
  <section class="card card--front" aria-label="Front of card">
    <h1 class="brand-name">TR Hair Studio</h1>
    <p class="contact">
      2751 Birchfield Rd.E. Cedarvale, QC H4R2M8<br>
      Phone. 555 614-2870<span class="sep">|</span>www.trhairexample.ca
    </p>
    <div class="social">
      <span class="social-item"><span class="social-dot"></span>trhair.salon</span>
      <span class="social-item"><span class="social-dot"></span>@TRsalonCuts</span>
    </div>
  </section>

  <section class="card card--back" aria-label="Back of card">
    <h2 class="appointment-title">Next Appointment:</h2>
    <div class="appointment-fields">
      <span class="field-label">Date</span>
      <span class="field-line field-line--date"></span>
      <span class="field-label">Time</span>
      <span class="field-line field-line--time"></span>
    </div>
    <div class="back-band"></div>
  </section>
</main>
</body>
</html>
```